Chicago Property Management Flyer

We need a brochure/flyer to market our property management services to Chicago property owners. I believe that my preference is single page, double sided, but a bi-fold or tri-fold format may also work. I have provided our logo, and some example images in case that is helpful. Refer to our website at http://www.velmorehq.net/ for more info.

Industry/Entity Type

Property Management

Font styles to use
Sans Serif

```html
<!DOCTYPE html>
<html lang="en">
<head>
<meta charset="utf-8">
<title>Velmore Property Management Flyer</title>
<link href="https://fonts.googleapis.com/css2?family=Oswald:wght@400;500&family=Lato:wght@400;700&family=Montserrat:wght@500;700&display=swap" rel="stylesheet">
<style>
  :root{
    --blue:#1e8cc4;
    --blue-dark:#14689a;
    --navy:#173a5c;
    --ink:#1d1d1d;
    --band:#2a2a2a;
    --white:#fff;
  }
  *{margin:0;padding:0;box-sizing:border-box}
  html,body{width:777px;height:1200px;overflow:hidden;background:#fff}
  .flyer{position:relative;width:777px;height:1200px;background:var(--white);overflow:hidden;font-family:'Lato',sans-serif;color:var(--ink)}
  .shapes{position:absolute;left:0;top:0}
  .brand{position:absolute;left:16px;top:160px;width:340px;text-align:center;white-space:nowrap}
  .brand-name{font-family:'Montserrat',sans-serif;font-weight:700;font-size:26px;color:var(--navy);letter-spacing:.3px;line-height:1}
  .brand-sub{font-family:'Montserrat',sans-serif;font-weight:500;font-size:16px;color:var(--navy);letter-spacing:4px;margin-top:6px}
  .tagline{position:absolute;left:29px;top:297px;width:270px;color:var(--white);font-size:21px;line-height:28px}
  .headline{position:absolute;left:20px;top:493px}
  .headline span{display:block;background:var(--ink);color:var(--white);font-family:'Oswald',sans-serif;font-weight:500;font-size:34px;line-height:47px;padding:0 8px;margin-bottom:7px;letter-spacing:1px;width:max-content}
  .feature{position:absolute;width:327px}
  .feature h3{font-family:'Oswald',sans-serif;font-weight:400;font-size:27px;color:var(--blue);line-height:34px;display:flex;align-items:center;gap:8px;margin-left:-28px;white-space:nowrap}
  .feature h3 svg{flex:none}
  .feature p{font-size:13.5px;line-height:17px;color:var(--ink);text-align:justify;margin-top:2px}
  .f1{left:51px;top:672px}
  .f2{left:51px;top:812px}
  .f3{left:51px;top:914px}
  .f4{left:430px;top:670px;width:302px}
  .f5{left:430px;top:812px;width:302px}
  .f6{left:430px;top:910px;width:302px}
  .f2 h3,.f3 h3,.f5 h3,.f6 h3{font-size:24px}
  .contact{position:absolute;left:36px;top:1083px;color:var(--white);font-size:19px;line-height:31px}
  .contact div{display:flex;align-items:center;gap:9px}
  .cta{position:absolute;right:35px;top:1060px;text-align:right;color:var(--navy);font-family:'Montserrat',sans-serif;font-weight:700;white-space:nowrap}
  .cta .label{font-size:28px;letter-spacing:1px;line-height:36px}
  .cta .phone{font-size:35px;color:var(--ink);line-height:46px}
</style>
</head>
<body>
<div class="flyer">
  <svg class="shapes" width="777" height="1200" viewBox="0 0 777 1200">
    <defs>
      <linearGradient id="photoTone" x1="0" y1="0" x2="1" y2="1">
        <stop offset="0" stop-color="#a84a32"/>
        <stop offset=".55" stop-color="#8e3b28"/>
        <stop offset=".8" stop-color="#5d8a3a"/>
        <stop offset="1" stop-color="#d9d9d6"/>
      </linearGradient>
      <linearGradient id="skyline" x1="0" y1="0" x2="0" y2="1">
        <stop offset="0" stop-color="#fff" stop-opacity="0"/>
        <stop offset="1" stop-color="#c9ccd0"/>
      </linearGradient>
      <linearGradient id="footBlue" x1="0" y1="0" x2="1" y2="0">
        <stop offset="0" stop-color="#1a6fa3"/>
        <stop offset="1" stop-color="#2b9ad1"/>
      </linearGradient>
    </defs>
    <rect x="0" y="960" width="777" height="140" fill="url(#skyline)" role="img" aria-label="Faded city skyline"/>
    <polygon points="408,0 438,0 330,408 300,408" fill="var(--blue)"/>
    <rect x="0" y="265" width="330" height="180" fill="var(--band)"/>
    <polygon points="318,265 340,265 300,445 278,445" fill="var(--blue)"/>
    <polygon points="430,0 777,0 777,640 322,418" fill="url(#photoTone)" role="img" aria-label="Photo of red brick apartment buildings behind an iron fence with lawn and sidewalk"/>
    <polygon points="300,410 322,418 777,640 777,660" fill="var(--band)"/>
    <polygon points="777,660 777,682 560,574 600,578" fill="var(--blue)"/>
    <polygon points="0,1074 398,1074 488,1169 777,1169 777,1200 0,1200" fill="url(#footBlue)"/>
    <polyline points="0,1071 400,1071 490,1166 777,1166" fill="none" stroke="var(--band)" stroke-width="5"/>
  </svg>

  <div class="brand">
    <div class="brand-name">VELMORE PROPERTY</div>
    <div class="brand-sub">MANAGEMENT</div>
  </div>

  <p class="tagline">Managing LHA / Section 8 rentals across Chicago for over a decade</p>

  <h1 class="headline">
    <span>LEVERAGE OUR EXPERIENCE</span>
    <span>AND EXPERTISE TO SUCCEED</span>
    <span style="width:390px">WITH YOUR PROPERTIES</span>
  </h1>

  <div class="feature f1">
    <h3><svg width="20" height="18" viewBox="0 0 20 18"><rect x="1" y="4" width="13" height="13" fill="none" stroke="#222" stroke-width="1.6"/><path d="M4 10l4 4L19 1" fill="none" stroke="#222" stroke-width="2.6"/></svg>Save Time and Headaches</h3>
    <p>We have a team in place to tackle all aspects of property management for you. Never worry about leasing, tenants, maintenance, regulations, etc.</p>
  </div>
  <div class="feature f2">
    <h3><svg width="20" height="18" viewBox="0 0 20 18"><rect x="1" y="4" width="13" height="13" fill="none" stroke="#222" stroke-width="1.6"/><path d="M4 10l4 4L19 1" fill="none" stroke="#222" stroke-width="2.6"/></svg>Reduce Expenses,Maximize Profits</h3>
    <p>Maximize your profits by benefitting from our economies of scale, systems and processes, specialized knowledge, industry network, and buying power</p>
  </div>
  <div class="feature f3">
    <h3><svg width="20" height="18" viewBox="0 0 20 18"><rect x="1" y="4" width="13" height="13" fill="none" stroke="#222" stroke-width="1.6"/><path d="M4 10l4 4L19 1" fill="none" stroke="#222" stroke-width="2.6"/></svg>Stay Informed</h3>
    <p style="font-size:14.5px;line-height:18px">With access to all of your property information, documentation, and financials through your online portal of our property management system you and your accountant can stay informed as needed</p>
  </div>
  <div class="feature f4">
    <h3><svg width="20" height="18" viewBox="0 0 20 18"><rect x="1" y="4" width="13" height="13" fill="none" stroke="#222" stroke-width="1.6"/><path d="M4 10l4 4L19 1" fill="none" stroke="#222" stroke-width="2.6"/></svg>Increase Income</h3>
    <p>With our experience and market knowledge we can establish optimal rent prices, lease apartments quickly, reduce turnover, and navigate complex housing agency processes to ensure maximum income to you.</p>
  </div>
  <div class="feature f5">
    <h3><svg width="20" height="18" viewBox="0 0 20 18"><rect x="1" y="4" width="13" height="13" fill="none" stroke="#222" stroke-width="1.6"/><path d="M4 10l4 4L19 1" fill="none" stroke="#222" stroke-width="2.6"/></svg>Maximize Your Investment Assets</h3>
    <p>Your properties are expensive assets with lots of potential. Put the right professionals in place to protect, maintain, and maximize their value.</p>
  </div>
  <div class="feature f6">
    <h3><svg width="20" height="18" viewBox="0 0 20 18"><rect x="1" y="4" width="13" height="13" fill="none" stroke="#222" stroke-width="1.6"/><path d="M4 10l4 4L19 1" fill="none" stroke="#222" stroke-width="2.6"/></svg>Grow Your Investment Portfolio</h3>
    <p style="text-align:left">With our management team focused on profitably managing your existing properties, we can then help you expand to future investments</p>
  </div>

  <div class="contact">
    <div><svg width="22" height="20" viewBox="0 0 22 20"><path d="M11 1L1 10h3v9h5v-6h4v6h5v-9h3z" fill="#fff"/></svg>1718 W. Harlan Ave Chicago IL 60699</div>
    <div style="font-size:18px"><svg width="22" height="16" viewBox="0 0 22 16"><rect x="1" y="1" width="20" height="14" fill="none" stroke="#fff" stroke-width="2"/><path d="M1 1l10 8 10-8" fill="none" stroke="#fff" stroke-width="2"/></svg>owen@velmorehq.net</div>
    <div style="font-size:18px"><svg width="22" height="22" viewBox="0 0 22 22"><g fill="none" stroke="#fff" stroke-width="1.5"><circle cx="11" cy="11" r="9.5"/><ellipse cx="11" cy="11" rx="4" ry="9.5"/><path d="M1.5 11h19M3 6h16M3 16h16"/></g></svg>www.velmorehq.net</div>
  </div>

  <div class="cta">
    <div class="label">CALL US NOW:</div>
    <div class="phone">555-201-4871</div>
  </div>
</div>
</body>
</html>
```